Major Australian Food and Wine Event Web Design Project

The project will consist of 3 designs
The homepage
A city hub page
A general content page

The main audience who will visit the website will be (in Order of importance:

1) Visitors
- Mainly women 24 – 54 years (they are the main ticket buyers)
- In a relationship – so will go to the show with their partner
- In a good paying job or home maker – and who have disposable income to spend $30 a ticker
- Enjoy food, wine and going out
- Looking for a fun day out – although an event that is about food and wine – it is an event that most people will go to and have a fun day out – not too pretentious

A smaller proportion of the audience will be:
2) Exhibitors & sponsors ( both prospective and existing)
3) Media

Objectives:

- Functionality on home page and sub pages needs to be updated, clear, easy to navigate and inject a sense of ‘fun’ – need to make it look more professional
- Need to incorporate the many things that need to be on the home page and sub pages in a visually appealing manner
- Ensure the ‘Cons’ above are considered and reflected in functionality and design
- To not be too focus on the colours (these can be changed) – but focus on the functionality and overall design opportunities.

Approach:

Keywords to describe the Bright Plate & Vine Fair:
Fun day out, discover, learn, indulge, entertaining

Other website examples:

Some great consumers event websites from the UK really make our website look basic and juvenile – and below are some examples of the presentation of how we would like our website to look like:

http://www.morselfairs-example.com/london/ This website is clean, includes good social media integration and exudes a sense of fun. Their content pages, such as the features landing page also presents options in a clear and visually appealing way with a series of boxes including image and text http://www.morselfairs-example.com/london/content/343/Features

http://www.homecraftexpo-example.com/ - this is also a great website – and it incorporates all the elements we would be looking for on our homepage – but the background/skin also includes a sense of fun and cheekiness. Subpages also are consistent.

Features

• Its a fun day that offers great value for money
• Caters to all visitors, regardless of different levels of knowledge or interest in food, wine and cooking.
• Sample great quality food and wine products from hundreds of reputable exhibitors
• Learn more through many of the shows feature activities (Celeb Theatre, Wine Theatre, Cooking & Cheese Classes)

Functionality & Structure:

In a user friendly, easy to view way, we need to incorporate the following functionality elements on home page:
- main header (that will incorporate our current creative) with a ‘fun’ skin
- navigation tabs/references (hone, location, tickets, blog, sign up, exhibitors)
- navigation/content banner (rotating)
- Area for small intro about the show
- News and highlight section
- New exhibitors section
- Obvious Ticket call to action
- Obvious sign up call to action
- Social media buttons or links ( really like the moving gifs on the Homecraftexpo-example.com site
- area for advertising (MREC size) to sell to exhibitors/sponsors
- Show dates for all 5 shows (maybe in main header)

Subpage layout is also important and needs to reflect the homepage – so would also like to see examples of how this would look and tie in with navigation – we generally have a lot of content on these pages, so clear navigation would be useful. – see below for further details of functionality for city Hubs

‘CITY HUB’ BRIEF
When navigating to each location the user will be taken to a ‘CITY HUB’ which should replicate design and content elements of a main HOME page, as well as reflect more specific information for each Show. Elements which must appear on this page are:
• FEATURES – which may be displayed in categories (in boxes, see appendix 1.0) which will link through to relevant content pages. Or in one box which will link through to a features page with all presented in boxes
• CHEFS – may be displayed as a separate icon box which will link to chefs page with bios, Celeb Theatre timetable etc.
• TICKETS – either a button or clear callout to purchase tickets
• PLAN YOUR DAY – may be displayed in a separate content box which will then link through to getting there, sample itineraries and downloadable pocket show guide for visitors to print before coming to the Show.
• WHO’S EXHIBITING – to link back to city specific exhibitor lists

Our current website is out of date and has the following inadequacies (www.brightplatefair-example.com.au) -

The homepage
A city hub page
A general content page

1) Visitors

3) Media

Objectives:

Approach:

To be perceived as a fun, entertaining event with something for everyone - website creative and navigation must reflect this.

Other website examples:

Features

- New exhibitors section

‘CITY HUB’ BRIEF

- Dated design/layout
- Homepage too text heavy
- No content boxes that can be used for different features/areas (eg. News, Exhibitors etc)
- Uninspiring colours and skin(eg. grey background), does not reflect ‘a fun day out’
- Limited presence of social media platforms and lacks ‘community’
- No continuity in sub pages
- main banner too big – takes up too much space on homepage

Requirements
Must have
• As per above brief.

In addition:
Floating social media buttons on side
Wrap around image
Drop down menu (specifically for the location nav item)

```html
<!DOCTYPE html>
<html lang="en">
<head>
<meta charset="utf-8">
<title>Bright Plate &amp; Vine Fair</title>
<link rel="stylesheet" href="https://fonts.googleapis.com/css2?family=Arimo:ital,wght@0,400;0,700;1,400&family=Noto+Serif:ital@1&display=swap">
<style>
:root{
  --accent:#e8401c;
  --accent-dark:#c8300f;
  --ink:#222;
  --muted:#666;
  --rule:#ddd;
  --page:#fff;
  --night:#0d0d0d;
  --footer:#232323;
  --grass:#4c8a22;
  --sky:#2f6fb8;
  --go:#7cb522;
}
*{box-sizing:border-box;margin:0;padding:0}
html,body{width:1022px;height:1200px;overflow:hidden;background:var(--night)}
body{font-family:"Arimo",Arial,sans-serif;color:var(--ink)}
.stage{position:relative;width:1106px;height:1298px;transform:scale(.92405);transform-origin:0 0}
.abs{position:absolute}
.page{left:80px;top:0;width:953px;height:1093px;background:var(--page)}

/* header */
.masthead{left:81px;top:0;width:951px;height:138px;background:linear-gradient(180deg,var(--sky) 0%,#9cc6ea 35%,#e9f3fb 60%,#8fc45a 78%,var(--grass) 100%)}
.brand{left:115px;top:0;width:173px;height:132px;background:#fff;border-radius:0 0 6px 6px;box-shadow:0 2px 6px rgba(0,0,0,.3);display:flex;align-items:center;justify-content:center;flex-direction:column;gap:8px;text-align:center}
.brand-dot{width:18px;height:18px;border-radius:50%;background:var(--accent)}
.brand-name{font-size:20px;font-weight:700;color:#222;line-height:1.15}
.tickets{left:484px;top:10px;width:92px;height:92px;border-radius:50%;background:radial-gradient(circle at 50% 35%,#f04a3a,#b81b12);border:3px solid #fff;box-shadow:0 3px 6px rgba(0,0,0,.35);color:#fff;text-align:center;padding-top:17px}
.tickets b{display:block;font-size:16px;line-height:1}
.tickets strong{display:block;font-size:20px;line-height:1.1}
.tickets em{font-style:normal;font-size:11px;color:#ffd23a;font-weight:700}
.dates{left:798px;top:0;width:219px;height:118px;background:#fff;border-radius:0 0 6px 6px;box-shadow:0 2px 6px rgba(0,0,0,.3);padding:2px 8px}
.dates div{display:flex;justify-content:space-between;font-size:12px;height:22px;line-height:22px;border-bottom:1px solid #e4e4e4;color:#222}
.dates div:last-child{border:0}

/* nav */
.nav{left:96px;top:152px;display:flex;align-items:center;height:26px}
.nav a{font-size:14px;color:#777;text-decoration:none;padding:0 14px;border-right:1px solid var(--rule);line-height:26px}
.nav a.on{color:var(--accent);font-weight:700;padding-left:0;display:flex;align-items:center;gap:8px}
.search{left:839px;top:152px;width:185px;height:27px;display:flex}
.search span{flex:1;border:1px solid #ccc;border-radius:3px 0 0 3px;font-size:12px;color:#999;padding:6px 12px}
.search i{width:30px;background:var(--go);border-radius:0 3px 3px 0;display:flex;align-items:center;justify-content:center}
.social{left:1033px;top:190px;width:38px;height:128px;background:#fff;padding:10px 0 0 0}
.social span{display:block;width:28px;height:28px;margin:0 0 10px 0;border-radius:3px}

/* hero */
.hero{left:90px;top:190px;width:933px;height:290px;border:1px solid #e2e2e2;background:linear-gradient(90deg,#e9e9e9 0%,#f7f7f7 60%,#fff 100%)}
.hero-photo{left:91px;top:191px;width:620px;height:288px;background:linear-gradient(90deg,#d9d9d9,#eeeeee 70%,rgba(255,255,255,0));}
.hero-band{left:91px;top:420px;width:420px;height:59px;background:linear-gradient(170deg,rgba(255,255,255,0) 30%,#f2b21b 55%,#e88a0c 75%,rgba(255,255,255,0) 90%)}
.hero-copy{left:726px;top:290px;width:258px}
.hero-copy h3{font-size:13px;color:var(--accent);margin-bottom:12px}
.hero-copy p{font-size:13px;line-height:20px;text-align:justify}
.dots{left:902px;top:460px;display:flex;gap:6px}
.dots i{width:14px;height:14px;border-radius:50%;background:#ccc}
.dots i:first-child{background:var(--accent)}

/* intro */
.welcome{left:111px;top:497px;width:580px}
.welcome h1{font-weight:400;font-size:27px;color:var(--accent);margin-bottom:12px}
.welcome p{font-size:12.5px;line-height:20px;letter-spacing:.2px;color:#333}
.welcome u{color:#333}
.section-title{font-size:17px;color:#555;border-bottom:1px solid #ccc;padding-bottom:1px}
.about{left:107px;top:729px;width:244px}
.about p{font-size:12px;line-height:16px;color:#666;text-align:justify;margin-top:8px;letter-spacing:.3px}
.testi{left:427px;top:729px;width:268px}
.testi .quote{left:48px;top:22px;width:222px;font-family:"Noto Serif",serif;font-style:italic;font-size:10px;line-height:20px;color:#888}
.testi .who{left:48px;top:126px;font-family:"Noto Serif",serif;font-size:11px;color:var(--accent)}
.testi svg{left:0;top:28px}

/* carousel */
.thumb{top:917px;width:133px;height:118px;border-radius:4px;background:radial-gradient(circle at 50% 45%,#e7dc8c,#c9a24a 55%,#7a5a2a);box-shadow:0 3px 5px rgba(0,0,0,.3)}
.thumb.on{border:4px solid var(--accent);top:903px;width:141px;height:126px;border-radius:5px}
.arrow{top:962px}

/* sidebar */
.news{left:714px;top:489px;width:298px;height:194px;border:1px solid #ccc;border-radius:5px;background:linear-gradient(#fff,#ececec);overflow:hidden}
.news header{height:41px;background:#3b3b3b;color:#fff;font-weight:700;font-size:16px;padding:12px 14px;position:relative}
.news header i{position:absolute;right:0;top:0;width:57px;height:41px;border-left:1px solid #555;background:#2e2e2e}
.news article{padding:6px 12px 0;border-bottom:1px dotted #ccc;margin:0 4px;padding-bottom:6px}
.news h4{font-weight:400;color:var(--accent);font-size:14px;margin-bottom:6px}
.news p{font-size:10px;line-height:13px;color:#666}
.news .more{text-align:right;font-size:11px;font-weight:700;color:#666;padding:12px 6px 0}
.signup{left:714px;top:694px;width:298px;height:111px;border-radius:6px;background:linear-gradient(#f2622a,#d8330b);color:#fff;padding:8px 14px}
.signup h2{font-size:22px;margin-bottom:6px}
.signup p{font-size:12px;line-height:14px;width:230px}
.signup .row{display:flex;gap:4px;margin-top:8px}
.signup .field{width:178px;height:23px;background:#fff;border-radius:2px;color:#222;font-size:12px;padding:4px 8px}
.signup .btn{width:80px;height:23px;background:#222;border-radius:2px;font-size:12px;padding:4px 10px}
.signup .env{right:10px;top:8px;width:44px;height:44px;border-radius:50%;background:#fff;border:3px solid #ddd}
.expo{left:714px;top:816px;width:299px;height:248px;background:#000;border-radius:4px;overflow:hidden}
.expo h3{color:#fff;font-size:16px;padding:9px 13px;height:36px}
.expo .ad{left:2px;top:36px;width:295px;height:210px;background:linear-gradient(135deg,#c81e10 0%,#8a1a0f 35%,#3b2a1c 70%,#6b5236 100%)}
.expo .big{left:12px;top:100px;font-size:40px;font-weight:700;line-height:40px;color:#fff;letter-spacing:-1px}
.expo .small{left:13px;top:190px;color:#fff;font-size:14px;line-height:17px}

/* footer */
.footer{left:80px;top:1093px;width:953px;height:179px;background:radial-gradient(circle at 880px 110px,#3a3a3a,var(--footer) 40%)}
.contact{left:80px;top:1110px;width:300px;color:#fff;font-size:10.5px;line-height:18px}
.contact h2{font-weight:400;font-size:20px;color:var(--accent);display:flex;align-items:center;gap:8px;margin-bottom:4px}
.contact b{font-weight:400;color:var(--accent)}
.links{top:1119px;font-size:10.5px;line-height:18.2px;color:#999}
.copy{left:927px;top:1121px;font-size:10.5px;color:var(--accent)}
</style>
</head>
<body>
<div class="stage">
  <div class="abs page"></div>

  <header>
    <div class="abs masthead" role="img" aria-label="Sky and green grass header scene"></div>
    <div class="abs brand"><span class="brand-dot"></span><span class="brand-name">Bright Plate<br>&amp; Vine Fair</span></div>
    <a class="abs tickets"><b>GET</b><strong>TICKETS</strong><em>*Premium</em></a>
    <div class="abs dates">
      <div><span>Melbourne</span><span>June 01-03, 2012</span></div>
      <div><span>Sydney</span><span>June 22-24, 2012</span></div>
      <div><span>Perth</span><span>July &nbsp;13-15, 2012</span></div>
      <div><span>Adelaide</span><span>October 12-14, 2012</span></div>
      <div><span>Brisbane</span><span>November 09-11, 2012</span></div>
    </div>
  </header>

  <nav class="abs nav">
    <a class="on"><svg width="19" height="18" viewBox="0 0 19 18"><path d="M9.5 1 1 8h3v9h4v-5h3v5h4V8h3z" fill="#e8401c"/></svg>Home</a>
    <a>Locations</a><a>Tickets</a><a style="padding:0 20px">Blog</a><a style="padding:0 20px">Signup</a><a>Exhibitors</a>
  </nav>
  <div class="abs search"><span>Search something...</span><i><svg width="14" height="14" viewBox="0 0 14 14"><circle cx="6" cy="6" r="4" stroke="#fff" stroke-width="2" fill="none"/><path d="M9 9l4 4" stroke="#fff" stroke-width="2"/></svg></i></div>
  <div class="abs social" aria-label="Social links">
    <span style="background:#f39220"></span><span style="background:#3b5a9a"></span><span style="background:#8cc7e6"></span>
  </div>

  <section>
    <div class="abs hero"></div>
    <div class="abs hero-photo" role="img" aria-label="Four chefs in white jackets standing together"></div>
    <div class="abs hero-band" role="img" aria-label="Plated dish with yellow garnish"></div>
    <div class="abs hero-copy">
      <h3>Simply dummy text of the printing</h3>
      <p>Lorem Ipsum has been the industry's standard dummy text ever since thes, when an unknown printer.Simply dummy text.</p>
    </div>
    <div class="abs dots"><i></i><i></i><i></i><i></i></div>
  </section>

  <main>
    <div class="abs welcome">
      <h1>Welcome to our website</h1>
      <p><strong>Simply dummy text of the printing and typesetting industry.</strong><br>
      Lorem Ipsum has been the industry's standard dummy text ever since thes, when an unknown printer.Simply dummy text of the <u>printing and typesetting industry</u>. Lorem Ipsum has been the indus-try's standard dummy text ever since thes, when an unknown printer.Simply dummy text of the printing and typesetting industry.</p>
      <p style="margin-top:20px">Standard dummy text ever since thes, when an unknown printer.Simply dummy text of the printing and typesetting industr</p>
    </div>

    <div class="abs about">
      <h2 class="section-title" style="font-weight:400">About &nbsp;Current &nbsp;Event</h2>
      <p style="margin-top:4px">Lorem Ipsum has been the industry's standard dummy text ever since thes, when an unknown printer.</p>
      <p style="margin-top:0">Lorem Ipsum has been the industry's standard dummy text ever since thes, when an unknown printer.</p>
    </div>

    <div class="abs testi" style="height:150px">
      <h2 class="section-title" style="font-weight:400;width:98px">Testimonials</h2>
      <svg class="abs" width="32" height="44" viewBox="0 0 32 44"><circle cx="16" cy="10" r="9" fill="#bbb"/><circle cx="16" cy="10" r="6" fill="#eee"/><path d="M14 18h4v10h-4z" fill="#444"/><path d="M4 44c0-10 5-15 12-15s12 5 12 15z" fill="#333"/></svg>
      <p class="abs quote">"Lorem Ipsum is simply dummy text of the printing and typesetting industry. Lorem Ips has been the industry's standard text ever since the 1500s, when an unknown printer dummy..."</p>
      <span class="abs who">Name client</span>
    </div>

    <svg class="abs arrow" style="left:101px" width="16" height="24" viewBox="0 0 16 24"><path d="M13 2 3 12l10 10" stroke="#bbb" stroke-width="3" fill="none"/></svg>
    <div class="abs thumb" style="left:132px" role="img" aria-label="Quiche with tomato"></div>
    <div class="abs thumb on" style="left:313px" role="img" aria-label="Quiche with tomato, selected"></div>
    <div class="abs thumb" style="left:502px" role="img" aria-label="Quiche with tomato"></div>
    <svg class="abs arrow" style="left:660px" width="16" height="24" viewBox="0 0 16 24"><path d="M3 2l10 10L3 22z" fill="#e8401c"/></svg>
  </main>

  <aside>
    <div class="abs news">
      <header>News &amp; Hightlight Section<i></i></header>
      <article><h4>News heading</h4><p>July is National Ice Cream Month! Cool off from the inside out with these delicious homemade ice cream.</p></article>
      <article style="border:0"><h4>News heading</h4><p>July is National Ice Cream Month! Cool off from the inside out with these delicious homemade ice cream.</p></article>
      <div class="more">More News...</div>
    </div>

    <div class="abs signup">
      <h2>Sign-Up</h2>
      <p>Lorem ipsum dolor sit ipsum Lorem ipsum dolor sit ipsum</p>
      <div class="row"><span class="field">Email</span><span class="btn">Sign-Up &#8250;</span></div>
      <div class="abs env"></div>
    </div>

    <div class="abs expo">
      <h3>Exhibitor Section</h3>
      <div class="abs ad" role="img" aria-label="Red velvet chair in an ornate room"></div>
      <div class="abs big">stays<br>with style</div>
      <div class="abs small">The finest places to rest in the world<br><i>Wayfarer Journal:</i> Top Picks 2010</div>
    </div>
  </aside>

  <footer>
    <div class="abs footer"></div>
    <div class="abs contact">
      <h2><svg width="38" height="34" viewBox="0 0 38 34"><rect x="1" y="8" width="36" height="25" fill="#eee"/><path d="M1 8l18 14L37 8" stroke="#999" fill="none"/><rect x="8" y="1" width="22" height="15" fill="#cfe0f0"/></svg>Contact Us</h2>
      Feel free to contact me or &nbsp;up below in the following<br>I will be in touch shortly.<br>
      <b>Address:</b> lorem ipsum Lorm ipsum<br>
      <b>Telephone:</b> +123-1234-5678<br>
      <b>&nbsp;FAX:</b> +458-4578<br>
      <b>Others:</b> +301 - 0125 - 01258<br>
      <b>E-mail:</b> &nbsp;mail@brightplate-example.com
    </div>
    <div class="abs links" style="left:392px">Bright Plate &amp; Vine Fair<br>Home<br>Melbourne<br>Sydney<br>Perth<br>Adelaide<br>Brisbane<br>Want to Exhibit?<br>Recipe Club</div>
    <div class="abs links" style="left:542px">Show Attractions<br>Celebrity Theatre<br>Cheese Masterclass<br>Cooking School<br>Decanter Bar<br>Restaurant<br>Wine Theatre<br>Exhibitor list<br>Floor plans</div>
    <div class="abs links" style="left:680px">Chef Bio's<br>Nora Ellery<br>Owen Lacklan<br>Theo Marandis<br>Remy Dufresne<br>Sam Colter<br>Jed Harlow<br>Recipe Club<br>Login</div>
    <div class="abs copy">Copyright text here</div>
  </footer>
</div>
</body>
</html>
```